Unisex Kids Baking Set Packaging

Need a design for the front panel of a box for a unisex kids baking set. Design should appeal to boys and girls. Front panel size is 315mm wide x 230mm tall. Should be sophisticated – but still kid-like/fun!

Target Market(s)

Kids

Requirements
Must have
• Sophistication yet fun
Nice to have
• colorful

```html
<!DOCTYPE html>
<html lang="en">
<head>
<meta charset="utf-8">
<title>Kids Baking Set – Front Panel</title>
<link rel="stylesheet" href="https://fonts.googleapis.com/css2?family=Chewy&family=Fredoka:wght@500;600;700&display=swap">
<style>
  :root {
    --teal: #14a89d;
    --orange: #f5921f;
    --purple: #4f3c98;
    --pink: #f8d7e8;
    --white: #ffffff;
    --trim: #d9342b;
  }
  html, body {
    margin: 0;
    width: 1200px;
    height: 1200px;
    overflow: hidden;
    background: var(--white);
  }
  .canvas { display: block; width: 1200px; height: 1200px; }
  .title-arc { font-family: "Fredoka", sans-serif; font-weight: 700; font-size: 84px; fill: var(--white); letter-spacing: 2px; }
  .age-label { font-family: "Fredoka", sans-serif; font-weight: 700; font-size: 44px; fill: var(--white); }
  .count-number { font-family: "Fredoka", sans-serif; font-weight: 700; font-size: 54px; fill: var(--white); }
  .count-caption { font-family: "Fredoka", sans-serif; font-weight: 600; font-size: 15px; fill: var(--white); letter-spacing: 1px; }
  .contents-heading { font-family: "Chewy", "Fredoka", sans-serif; font-weight: 500; font-size: 20px; fill: var(--orange); }
  .contents-item text { font-family: "Chewy", "Fredoka", sans-serif; font-weight: 500; font-size: 16px; fill: var(--white); }
  .badge-big { font-family: "Fredoka", sans-serif; font-weight: 700; font-size: 38px; fill: var(--white); }
  .badge-small { font-family: "Fredoka", sans-serif; font-weight: 700; font-size: 15px; fill: var(--white); }
</style>
</head>
<body>
<svg class="canvas" viewBox="0 0 1200 1200" xmlns="http://www.w3.org/2000/svg">
  <defs>
    <path id="title-path" d="M 409 674 A 225 225 0 1 1 831 674"/>
    <path id="count-path" d="M 164 662 A 44 44 0 0 0 248 662"/>
    <linearGradient id="cups-tone" x1="0" y1="0" x2="1" y2="1">
      <stop offset="0" stop-color="#9a7ad8"/><stop offset="0.5" stop-color="#3fa0e0"/><stop offset="1" stop-color="#d8262f"/>
    </linearGradient>
    <linearGradient id="whisk-tone" x1="0" y1="0" x2="1" y2="0">
      <stop offset="0" stop-color="#b8bcc2"/><stop offset="1" stop-color="#e5b84a"/>
    </linearGradient>
    <linearGradient id="spoons-tone" x1="0" y1="0" x2="1" y2="1">
      <stop offset="0" stop-color="#dfeb5a"/><stop offset="0.5" stop-color="#3fb4e6"/><stop offset="1" stop-color="#e96aa8"/>
    </linearGradient>
    <linearGradient id="liners-tone" x1="0" y1="0" x2="0" y2="1">
      <stop offset="0" stop-color="#e78cc4"/><stop offset="1" stop-color="#b986dc"/>
    </linearGradient>
  </defs>

  <!-- front panel -->
  <rect class="panel" x="96" y="233" width="1008" height="734" fill="var(--teal)"/>
  <rect class="trim-line" x="127.5" y="255.5" width="945" height="690" fill="none" stroke="var(--trim)" stroke-width="0.6"/>

  <!-- age tab -->
  <path class="age-tab" d="M 946 232 H 1036 V 317 A 45 45 0 0 1 946 317 Z" fill="var(--purple)"/>
  <text class="age-label" x="991" y="334" text-anchor="middle">6+</text>

  <!-- central medallion -->
  <circle class="medallion-ring" cx="620" cy="597" r="314" fill="var(--orange)"/>
  <circle class="hero-photo" cx="620" cy="597" r="203" fill="var(--pink)" role="img" aria-label="Photo of two smiling children in chef hats and white aprons holding a slotted turner and a rolling pin"/>

  <!-- product shots -->
  <rect class="product-cups" x="312" y="612" width="116" height="100" rx="46" fill="url(#cups-tone)" opacity="0.92" role="img" aria-label="Nested rainbow measuring cups"/>
  <rect class="product-whisk" x="322" y="738" width="272" height="34" rx="17" transform="rotate(28 322 738)" fill="url(#whisk-tone)" role="img" aria-label="Whisk with rainbow silicone wires"/>
  <rect class="product-heart" x="588" y="764" width="88" height="84" rx="30" fill="#d8262f" opacity="0.85" role="img" aria-label="Heart cookie cutter"/>
  <rect class="product-flower" x="648" y="834" width="90" height="84" rx="34" fill="#a35bb5" opacity="0.85" role="img" aria-label="Flower cookie cutter"/>
  <rect class="product-spoons" x="758" y="674" width="156" height="160" rx="50" fill="url(#spoons-tone)" opacity="0.9" role="img" aria-label="Rainbow measuring spoons"/>
  <rect class="product-liners" x="828" y="588" width="98" height="108" rx="40" fill="url(#liners-tone)" role="img" aria-label="Silicone baking cups"/>

  <!-- title -->
  <text class="title-arc"><textPath href="#title-path" startOffset="50%" text-anchor="middle">KIDS BAKING SET</textPath></text>

  <!-- piece count badge -->
  <circle class="count-badge" cx="206" cy="658" r="54" fill="var(--orange)"/>
  <text class="count-number" x="206" y="671" text-anchor="middle">24</text>
  <text class="count-caption"><textPath href="#count-path" startOffset="50%" text-anchor="middle" dominant-baseline="hanging">PIECE SET</textPath></text>

  <!-- contents list -->
  <g class="contents">
    <text class="contents-heading" x="163" y="746">WHAts inside?</text>
    <g class="contents-item">
      <text x="162" y="772">•</text><text x="181" y="772">Measuring Cups</text>
      <text x="162" y="791">•</text><text x="181" y="791">Measuring Spoons</text>
      <text x="162" y="810">•</text><text x="181" y="810">Whisk</text>
      <text x="162" y="829">•</text><text x="181" y="829">Rolling Pin</text>
      <text x="162" y="848">•</text><text x="181" y="848">Spatula</text>
      <text x="162" y="867">•</text><text x="181" y="867">Slotted Turner</text>
      <text x="162" y="886">•</text><text x="181" y="886">Baking Cups</text>
      <text x="162" y="905">•</text><text x="181" y="905">Cookie Cutters</text>
    </g>
  </g>

  <!-- callout badges -->
  <circle class="callout" cx="991" cy="727" r="54" fill="var(--purple)"/>
  <text class="badge-big" x="991" y="731" text-anchor="middle">GET</text>
  <text class="badge-small" x="991" y="756" text-anchor="middle">CREATIVE</text>

  <circle class="callout" cx="991" cy="854" r="54" fill="var(--purple)"/>
  <text class="badge-big" x="991" y="852" text-anchor="middle" font-size="34">HAVE</text>
  <text class="badge-big" x="991" y="886" text-anchor="middle" font-size="34">FUN</text>
</svg>
</body>
</html>
```